BrightHarbor Flowchart Marketing Flyer

We are an MSP IT company. We have created a flowchart that we would like jazzed up to use in marketing new customers. The flowchart is a visual for prospective clients to see, in a simple way, what our process is. The flowchart should be 8.5"x11". We do not want the template of the flowchart altered (no boxes moved around) but would like something visually appealing and clean looking. Our office colors are lime green, royal blue, with accent colors of orange and purple. We would like the colors incorporated into the design. The design should be modern. This flyer is not going to be mass mailed. It will be handed to a prospective client in a face to face meeting.
Updates

I have uploaded our company logo to my brief in a couple of formats. One of the designers requested this. Great idea! I apologize for not providing it to begin with - it's my first time using this Website and the first time I have been assigned a project.

I was not able to view over the weekend as I did not have access to my work computer. Also need to review with the rest of management team on Thursday 6/28

Target Market(s)

Potential clients for an MSP IT company

Industry/Entity Type

It Company

Requirements
Must have
• The template itself we don't want changed. In other words we don't want the boxes moved around.
Nice to have
• Text, lines, shading and color of boxes can be changed. Not all colors mentioned in the brief need to be used. Would like it easy on the eye.

```html
<!DOCTYPE html>
<html lang="en">
<head>
<meta charset="utf-8">
<title>BrightHarbor Process Flyer</title>
<link rel="stylesheet" href="https://fonts.googleapis.com/css2?family=Archivo:ital,wght@1,900&family=Cabin:wght@400;500;600&display=swap">
<style>
  :root {
    --royal: #0f5aa6;
    --green: #14992f;
    --orange: #f5a300;
    --orange-deep: #e39400;
    --purple: #82007e;
    --ink: #1e1e1e;
    --page: #ffffff;
    --stage: #656565;
  }
  html, body {
    margin: 0;
    width: 1200px;
    height: 1200px;
    overflow: hidden;
    background: var(--stage);
  }
  .flyer {
    position: absolute;
    left: 88px;
    top: 204px;
    width: 1024px;
    height: 792px;
    display: block;
    box-shadow: 0 6px 14px rgba(0,0,0,.35);
  }
  .title {
    font-family: "Archivo", "Arial Black", sans-serif;
    font-weight: 900;
    font-style: italic;
    fill: var(--royal);
  }
  .step-label, .wheel-label {
    font-family: "Cabin", sans-serif;
    font-weight: 500;
    fill: #fff;
    text-anchor: middle;
  }
  .hub-label {
    font-family: "Cabin", sans-serif;
    font-weight: 600;
    fill: var(--royal);
    text-anchor: middle;
  }
  .bullet-text {
    font-family: "Cabin", sans-serif;
    font-size: 18px;
    fill: var(--ink);
  }
  .plan-text { font-size: 19px; }
  .flow-line {
    fill: none;
    stroke: #111;
    stroke-width: 3;
    stroke-dasharray: 9 6;
  }
  .wheel-segment { stroke: #fff; stroke-width: 10; stroke-linejoin: round; }
  .brand-name {
    font-family: "Cabin", sans-serif;
    font-weight: 600;
    font-size: 52px;
    fill: #fff;
  }
</style>
</head>
<body>
<svg class="flyer" viewBox="110 255 1280 990" xmlns="http://www.w3.org/2000/svg">
  <defs>
    <radialGradient id="hub-fill" cx="45%" cy="35%" r="65%">
      <stop offset="0" stop-color="#ffffff"/>
      <stop offset="1" stop-color="#c9c9c9"/>
    </radialGradient>
    <radialGradient id="step-green" cx="50%" cy="35%" r="65%">
      <stop offset="0" stop-color="#1bb23a"/><stop offset="1" stop-color="#0c7d22"/>
    </radialGradient>
    <radialGradient id="step-orange" cx="50%" cy="35%" r="65%">
      <stop offset="0" stop-color="#f5ab1a"/><stop offset="1" stop-color="#d78a00"/>
    </radialGradient>
    <radialGradient id="step-purple" cx="50%" cy="40%" r="65%">
      <stop offset="0" stop-color="#b012b0"/><stop offset="1" stop-color="#730070"/>
    </radialGradient>
    <filter id="soft-shadow" x="-20%" y="-20%" width="140%" height="140%">
      <feDropShadow dx="0" dy="2" stdDeviation="4" flood-opacity=".3"/>
    </filter>
  </defs>

  <rect class="page" x="110" y="255" width="1280" height="990" fill="var(--page)"/>

  <!-- Heading -->
  <text class="title" x="160" y="372" font-size="92">BrightHarbor</text>
  <text class="title" x="160" y="474" font-size="100">Process</text>

  <!-- Onboarding flow -->
  <path class="flow-line" d="M400 579 H238 Q215 579 215 602 V808 Q215 832 240 832 H400"/>
  <path class="flow-line" d="M556 836 H744 Q768 836 768 860 V1058 Q768 1082 744 1082 H556"/>

  <g class="step step-assess" filter="url(#soft-shadow)">
    <circle cx="478" cy="577" r="78" fill="#fff"/>
    <circle cx="478" cy="577" r="72" fill="url(#step-green)"/>
  </g>
  <text class="step-label" x="478" y="569" font-size="27">Assess</text>
  <text class="step-label" x="478" y="601" font-size="27">Alignment</text>

  <g class="bullets bullets-assess">
    <circle cx="357" cy="679" r="5" fill="var(--green)"/>
    <text class="bullet-text" x="376" y="685">Review Technology Philosophy</text>
    <circle cx="357" cy="706" r="5" fill="var(--green)"/>
    <text class="bullet-text" x="372" y="714">Share Proprietary Method</text>
    <circle cx="357" cy="737" r="5" fill="var(--green)"/>
    <text class="bullet-text" x="372" y="743">Assess Organizational Fit</text>
  </g>

  <g class="step step-onboard" filter="url(#soft-shadow)">
    <circle cx="477" cy="842" r="78" fill="#fff"/>
    <circle cx="477" cy="842" r="72" fill="url(#step-orange)"/>
  </g>
  <text class="step-label" x="477" y="833" font-size="27">On</text>
  <text class="step-label" x="477" y="865" font-size="27">Boarding</text>

  <g class="bullets bullets-onboard">
    <circle cx="224" cy="941" r="5" fill="var(--orange-deep)"/>
    <text class="bullet-text" x="240" y="948">Establish Expectations</text>
    <circle cx="224" cy="967" r="5" fill="var(--orange-deep)"/>
    <text class="bullet-text" x="240" y="974">Service Provider Transition</text>
    <circle cx="495" cy="941" r="5" fill="var(--orange-deep)"/>
    <text class="bullet-text" x="512" y="948">Cybersecurity Review</text>
    <circle cx="495" cy="967" r="5" fill="var(--orange-deep)"/>
    <text class="bullet-text" x="512" y="974">Backup/Protection Strategy</text>
  </g>

  <g class="step step-evaluate" filter="url(#soft-shadow)">
    <circle cx="475" cy="1066" r="78" fill="#fff"/>
    <circle cx="475" cy="1066" r="72" fill="url(#step-purple)"/>
  </g>
  <text class="step-label" x="475" y="1054" font-size="27">30 Day</text>
  <text class="step-label" x="475" y="1086" font-size="27">Evaluation</text>

  <g class="bullets bullets-evaluate">
    <circle cx="224" cy="1165" r="5" fill="var(--purple)"/>
    <text class="bullet-text" x="237" y="1172">Develop IT Playbook</text>
    <circle cx="224" cy="1190" r="5" fill="var(--purple)"/>
    <text class="bullet-text" x="237" y="1197">Major Risk Identification</text>
    <circle cx="500" cy="1165" r="5" fill="var(--purple)"/>
    <text class="bullet-text" x="512" y="1172">Observe &amp; Document Trends</text>
    <circle cx="500" cy="1190" r="5" fill="var(--purple)"/>
    <text class="bullet-text" x="512" y="1197">Standards Alignment Plan</text>
  </g>

  <!-- Strategic plan wheel -->
  <circle cx="1072" cy="570" r="266" fill="#fff" filter="url(#soft-shadow)"/>
  <path class="wheel-segment" fill="var(--green)"  d="M975.4 544.1 Q896.7 601 825.7 504 A255 255 0 0 1 1138 323.7 Q1041 394.7 1097.9 473.4 A100 100 0 0 0 975.4 544.1Z"/>
  <path class="wheel-segment" fill="var(--royal)"  d="M1097.9 473.4 Q1041 394.7 1138 323.7 A255 255 0 0 1 1318.3 636 Q1247.3 539 1168.6 595.9 A100 100 0 0 0 1097.9 473.4Z"/>
  <path class="wheel-segment" fill="var(--orange)" d="M1168.6 595.9 Q1247.3 539 1318.3 636 A255 255 0 0 1 1006 816.3 Q1103 745.3 1046.1 666.6 A100 100 0 0 0 1168.6 595.9Z"/>
  <path class="wheel-segment" fill="var(--purple)" d="M1046.1 666.6 Q1103 745.3 1006 816.3 A255 255 0 0 1 825.7 504 Q896.7 601 975.4 544.1 A100 100 0 0 0 1046.1 666.6Z"/>
  <circle cx="1072" cy="570" r="96" fill="#fff"/>
  <circle cx="1072" cy="570" r="90" fill="url(#hub-fill)"/>

  <text class="wheel-label" x="983" y="403" font-size="28">Risk</text>
  <text class="wheel-label" x="983" y="438" font-size="28">Assessment</text>
  <text class="wheel-label" x="1218" y="489" font-size="28">Strategy</text>
  <text class="wheel-label" x="921" y="661" font-size="28">Budget</text>
  <text class="wheel-label" x="1140" y="716" font-size="28">Standards</text>
  <text class="wheel-label" x="1140" y="751" font-size="28">Alignment</text>

  <text class="hub-label" x="1072" y="540" font-size="25">Ongoing</text>
  <text class="hub-label" x="1072" y="571" font-size="25">Strategic Plan</text>
  <text class="hub-label" x="1072" y="602" font-size="25">&amp; Execution</text>

  <g class="bullets bullets-plan">
    <circle cx="927" cy="880" r="3.5" fill="#3a6fd8"/>
    <text class="bullet-text plan-text" x="940" y="887">Develop &amp; Execute Annual Strategic Plan</text>
    <circle cx="927" cy="909" r="3.5" fill="#3a6fd8"/>
    <text class="bullet-text plan-text" x="940" y="916">Risk Assessment, Ranking, Mitigation</text>
    <circle cx="927" cy="938" r="3.5" fill="#3a6fd8"/>
    <text class="bullet-text plan-text" x="940" y="945">Prioritize Investments</text>
    <circle cx="927" cy="967" r="3.5" fill="#3a6fd8"/>
    <text class="bullet-text plan-text" x="940" y="974">Develop 5 Year Budget</text>
    <circle cx="927" cy="996" r="3.5" fill="#3a6fd8"/>
    <text class="bullet-text plan-text" x="940" y="1003">HarborSolution™ Standard Alignment</text>
  </g>

  <!-- Footer band and brand panel -->
  <rect class="footer-band" x="110" y="1220" width="780" height="25" fill="var(--royal)"/>
  <rect class="brand-panel" x="881" y="1040" width="509" height="205" fill="var(--royal)"/>
  <circle cx="985" cy="1138" r="16" fill="#fff"/>
  <text class="brand-name" x="1015" y="1157">Bayline IT</text>
</svg>
</body>
</html>
```